Folder Design: Mobile Laboratory Service

Need a folder designed for a Mobile Laboratory Service. Folder needs to be very professional and will be used to hold brochure, contract and business card of business. Logos of the company are attached.

Industry/Entity Type

Healthcare

```html
<!DOCTYPE html>
<html lang="en">
<head>
<meta charset="utf-8">
<title>Fieldline Lab Services – Presentation Folder</title>
<link rel="stylesheet" href="https://fonts.googleapis.com/css2?family=Cinzel:wght@400;700&family=Poppins:wght@400;600&display=swap">
<style>
  :root {
    --stage: #383e45;
    --paper: #ffffff;
    --brand-blue: #3f97e6;
    --brand-blue-light: #5bb6f2;
    --brand-blue-deep: #2f7fd8;
    --navy: #0a1528;
    --ink-white: #ffffff;
  }
  html, body {
    margin: 0;
    width: 677px;
    height: 1200px;
    overflow: hidden;
    background: var(--stage);
  }
  .folder-dieline {
    position: absolute;
    left: 18px;
    top: 324px;
    width: 640px;
    height: 551px;
    display: block;
  }
  .title { font-family: "Cinzel", serif; font-weight: 700; font-size: 46px; fill: var(--navy); }
  .site-url { font-family: "Poppins", sans-serif; font-weight: 600; font-size: 15px; letter-spacing: 2.2px; fill: var(--ink-white); }
  .site-url--pocket { fill: var(--navy); }
  .contact { font-family: "Poppins", sans-serif; font-size: 12px; fill: var(--ink-white); text-anchor: middle; }
  .brand-name { font-family: "Poppins", sans-serif; font-weight: 600; }
  .brand-name--cover { font-size: 30px; fill: var(--brand-blue); }
  .brand-name--badge { font-size: 20px; fill: var(--ink-white); text-anchor: middle; }
  .brand-name--pocket { font-size: 22px; fill: var(--ink-white); }
  .icon-dot { fill: var(--navy); }
  .icon-line { fill: none; stroke: var(--ink-white); stroke-width: 1.6; stroke-linecap: round; stroke-linejoin: round; }
</style>
</head>
<body>
<svg class="folder-dieline" viewBox="0 0 1120 965" xmlns="http://www.w3.org/2000/svg" aria-label="Fieldline Lab Services pocket folder, flat layout">
  <defs>
    <linearGradient id="lab-blue" x1="0" y1="0" x2="0" y2="1">
      <stop offset="0" stop-color="#55b3f0"/>
      <stop offset="0.55" stop-color="#4aa3ea"/>
      <stop offset="1" stop-color="#3e94e4"/>
    </linearGradient>
    <linearGradient id="tube-fade" x1="0" y1="0" x2="1" y2="0">
      <stop offset="0" stop-color="#ffffff" stop-opacity="0"/>
      <stop offset="0.4" stop-color="#e4ecf7"/>
      <stop offset="1" stop-color="#eef0fa"/>
    </linearGradient>
    <clipPath id="cover-clip"><rect x="36" y="0" width="1048" height="965"/></clipPath>
  </defs>

  <!-- pocket side flaps -->
  <path class="pocket-flap" d="M36 728 L0 745 L0 955 L36 965 Z" fill="var(--brand-blue-deep)"/>
  <path class="pocket-flap" d="M1084 728 L1120 745 L1120 955 L1084 965 Z" fill="var(--brand-blue-deep)"/>

  <g clip-path="url(#cover-clip)">
    <rect class="paper" x="36" y="0" width="1048" height="965" fill="var(--paper)"/>
    <rect role="img" aria-label="Photo of glass test tubes in a rack" x="760" y="0" width="324" height="560" fill="url(#tube-fade)"/>
    <path class="arc-band" d="M36 530 Q560 40 1084 540 L1084 965 L36 965 Z" fill="var(--navy)"/>
    <path role="img" aria-label="Blue-toned photo of lab glassware and beakers" d="M36 552 Q560 78 1084 556 L1084 965 L36 965 Z" fill="url(#lab-blue)"/>
    <path d="M526 965 L560 728 L600 965 Z" fill="var(--stage)"/>
  </g>

  <!-- cover brand name -->
  <g class="brand-cover">
    <circle cx="644" cy="132" r="9" fill="var(--brand-blue)"/>
    <text class="brand-name brand-name--cover" x="662" y="143">Fieldline</text>
  </g>

  <!-- badge on arc -->
  <circle cx="306" cy="345" r="68" fill="var(--navy)"/>
  <text class="brand-name brand-name--badge" x="306" y="352">Fieldline</text>

  <!-- contact icons -->
  <g class="contact-icons">
    <circle class="icon-dot" cx="242" cy="481" r="13"/>
    <path class="icon-line" d="M242 488 C237 482 237 479 237 477 A5 5 0 0 1 247 477 C247 479 247 482 242 488 Z"/>
    <circle class="icon-dot" cx="284" cy="481" r="13"/>
    <path class="icon-line" d="M279 475 L282 474 L284 478 L282 480 Q284 484 287 485 L289 483 L293 485 L292 488 Q284 489 279 475 Z"/>
    <circle class="icon-dot" cx="327" cy="481" r="13"/>
    <rect class="icon-line" x="320" y="476" width="14" height="10" rx="1"/>
    <path class="icon-line" d="M320 477 L327 482 L334 477"/>
    <circle class="icon-dot" cx="371" cy="481" r="13"/>
    <circle class="icon-line" cx="371" cy="481" r="7"/>
    <path class="icon-line" d="M364 481 H378 M371 474 Q366 481 371 488 M371 474 Q376 481 371 488"/>
  </g>

  <!-- contact details -->
  <text class="contact" x="307" y="544">23456 Lorem Ipsum City</text>
  <text class="contact" x="307" y="558">lorem Ipsum 767676</text>
  <text class="contact" x="307" y="588">555 0142 3377</text>
  <text class="contact" x="307" y="614">info@fieldlinelab.com</text>
  <text class="contact" x="307" y="643">www.fieldlinelab.com</text>

  <!-- title block -->
  <text class="title" x="616" y="484">FIELDLINE</text>
  <text class="title" x="616" y="528">LAB</text>
  <text class="title" x="616" y="572">SERVICES</text>
  <line x1="616" y1="604" x2="930" y2="604" stroke="#ffffff" stroke-opacity="0.6" stroke-width="1"/>
  <line x1="652" y1="604" x2="682" y2="604" stroke="#ffffff" stroke-width="3"/>
  <text class="site-url" x="618" y="643">www.fieldlinelab.com</text>

  <!-- pocket panels, printed upside down -->
  <text class="site-url site-url--pocket" x="299" y="850" text-anchor="middle" transform="rotate(180 299 845)">www.fieldlinelab.com</text>
  <g transform="rotate(180 824 853)">
    <text class="brand-name brand-name--pocket" x="824" y="861" text-anchor="middle">Fieldline</text>
  </g>
</svg>
</body>
</html>
```